Weight loss surgery restaurant card

We need to create a card for patients who have undergone weight loss surgery to take to restaurants so they can request smaller meals. These patients have had surgery on their stomach so that they can only consume half to one cup of food at a time. So normal sized restaurant meals are way too big (and cost a lot). This card they can present to the restaurant to communicate the fact that they have had weight loss surgery and therefore request a smaller meal portion at reduced cost

Target Market(s)

Restaurants serving weight loss surgery patients

Industry/Entity Type

Health Care

Contact Information for Business Card

This will be a plastic card similar to business card size.

Requirements
Must have
• The front of the card should include the following text:
• The individual bearing this card has undergone weight loss surgery.
• This surgery restricts portion sizes to between half and one cup of food at a time.
• Please give consideration to allowing smaller portions of your regular meals to be ordered to reduce wastage and excess costs.
• Example: a half size portion priced at two thirds of usual cost.
• The back of the card will have spaces for the person to write certain information. These are the categories that can be filled in by hand:
• Name:
• Procedure performed:
• Date of procedure (month/year):
• Treating Clinic Name:
• Treating Clinic Signature:
• Somewhere down the bottom should be something along the lines of:
• supplied from bernardwhitlow.com.au
Nice to have
• A nice design with imagery/colours etc ... not just the text on a white background! Bright attractive colours preferred.
• I have uploaded my logo ... a roughly triangular image followed by my name etc. The triangular logo image could be used somewhere on the card and this logo can be interchangeable for other clinics who purchase the card.
• **Please note that I don't want my name to be included as part of the logo on the card ... just use the triangular image on the side of the logo without the following name**
• Also, the colouring of the card does not have to reflect my logo colours as I am anticipating interchanging this logo with other logos if other clinics choose to adopt the card. I am interested to see other, more generic, colour choices as well as my logo colours

```html
<!DOCTYPE html>
<html lang="en">
<head>
<meta charset="utf-8">
<title>Weight Loss Surgery Restaurant Card</title>
<link href="https://fonts.googleapis.com/css2?family=Source+Sans+3:wght@400;600&display=swap" rel="stylesheet">
<style>
  :root {
    --green: #2fb27a;
    --blue: #3d6ef2;
    --ink: #111111;
    --rule: #eef1ef;
    --paper: #ffffff;
  }
  * { margin: 0; padding: 0; box-sizing: border-box; }
  html, body { width: 1200px; height: 1000px; overflow: hidden; background: var(--paper); }
  body { font-family: "Source Sans 3", "Myriad Pro", sans-serif; position: relative; }

  .side-label {
    position: absolute; left: 30px; width: 44px;
    color: var(--blue); font-size: 46px; line-height: 52px;
    text-align: center; font-weight: 400;
  }
  .side-label--front { top: 74px; }
  .side-label--back { top: 566px; }

  .card-divider {
    position: absolute; left: 0; top: 458px; width: 1200px; height: 1px;
    background: var(--rule);
  }

  .front-message {
    position: absolute; left: 187px; top: 28px; width: 800px;
    text-align: center; color: var(--green);
    font-size: 24px; line-height: 34.4px;
  }

  .clinic-mark {
    position: absolute; display: flex; align-items: center; gap: 12px;
    color: var(--green); font-weight: 600;
  }
  .clinic-mark__dot { border-radius: 50%; background: var(--green); flex: none; }
  .clinic-mark__text { display: flex; flex-direction: column; line-height: 1; }
  .clinic-mark--front { left: 412px; top: 322px; }
  .clinic-mark--front .clinic-mark__dot { width: 56px; height: 56px; }
  .clinic-mark--front .clinic-mark__name { font-size: 31px; letter-spacing: 1px; }
  .clinic-mark--front .clinic-mark__role { font-size: 12px; letter-spacing: 1px; margin-top: 4px; }
  .clinic-mark--footer { left: 460px; top: 910px; }
  .clinic-mark--footer .clinic-mark__dot { width: 50px; height: 50px; }
  .clinic-mark--footer .clinic-mark__name { font-size: 26px; letter-spacing: 1px; }
  .clinic-mark--footer .clinic-mark__role { font-size: 10px; letter-spacing: 1px; margin-top: 4px; }

  .patient-fields { position: absolute; left: 192px; top: 524px; width: 816px; list-style: none; }
  .patient-fields__row {
    display: flex; align-items: flex-end; height: 47.2px;
    color: var(--green); font-size: 30px;
  }
  .patient-fields__label { width: 425px; line-height: 1; }
  .patient-fields__line { flex: 1; border-bottom: 2px solid var(--green); margin-bottom: -2px; }

  .supplier-note {
    position: absolute; left: 0; top: 876px; width: 1200px;
    text-align: center; color: var(--ink); font-size: 19px;
  }
</style>
</head>
<body>
  <div class="side-label side-label--front">F<br>R<br>O<br>N<br>T</div>

  <section class="card-front">
    <p class="front-message">
      The individual bearing this card has undergone weight loss surgery.<br>
      Around 500,00 of these procedures are performed<br>
      around the world every year.<br>
      The surgery restricts portion sizes to between half and<br>
      one cup of food at a time.<br>
      Please give consideration to allowing smaller portions of your regular<br>
      meals to be ordered to reduce waste and excess costs.<br>
      * Example: a half size portion at two thirds of usual cost.
    </p>
    <div class="clinic-mark clinic-mark--front">
      <span class="clinic-mark__dot"></span>
      <span class="clinic-mark__text">
        <span class="clinic-mark__name">BERNARD WHITLOW</span>
        <span class="clinic-mark__role">GENERAL, UPPER GI &amp; BARIATRIC SURGEON</span>
      </span>
    </div>
  </section>

  <div class="card-divider"></div>

  <div class="side-label side-label--back">B<br>A<br>C<br>K</div>

  <section class="card-back">
    <ul class="patient-fields">
      <li class="patient-fields__row"><span class="patient-fields__label">Patient name:</span><span class="patient-fields__line"></span></li>
      <li class="patient-fields__row"><span class="patient-fields__label">Procedure performed:</span><span class="patient-fields__line"></span></li>
      <li class="patient-fields__row"><span class="patient-fields__label">Date of procedure:</span><span class="patient-fields__line"></span></li>
      <li class="patient-fields__row"><span class="patient-fields__label">Treating clinic name:</span><span class="patient-fields__line"></span></li>
      <li class="patient-fields__row"><span class="patient-fields__label">Treating clinic signature:</span><span class="patient-fields__line"></span></li>
    </ul>
    <p class="supplier-note">Purchased through www.bernardwhitlow.com.au</p>
    <div class="clinic-mark clinic-mark--footer">
      <span class="clinic-mark__dot"></span>
      <span class="clinic-mark__text">
        <span class="clinic-mark__name">BERNARD WHITLOW</span>
        <span class="clinic-mark__role">GENERAL, UPPER GI &amp; BARIATRIC SURGEON</span>
      </span>
    </div>
  </section>
</body>
</html>
```